Resume for higher management position in a mechanical/consultant industries application*

I would like to use this resume for getting a higher position interview possibilities. My skills are multi-cultural negotiation, mechanical industry sales, outsourcing to Asia, ability to manage the agent/reseller system, well team player. multi-language Chinese/English/German specialized. Please make the design, professional, comfortable to read atmosphere.

Target Market(s)

management position, sales related

Font styles to use
Serif
Sans Serif

```html
<!DOCTYPE html>
<html lang="en">
<head>
<meta charset="utf-8">
<title>Wei-Lin Hsu – Sales Manager Resume</title>
<link href="https://fonts.googleapis.com/css2?family=Arimo:wght@400;700&family=Open+Sans:wght@400&display=swap" rel="stylesheet">
<style>
  :root{
    --ink:#454545;
    --dark:#444444;
    --paper:#ffffff;
    --muted:#bdbdbd;
    --photo:#b9b9b9;
  }
  *{margin:0;padding:0;box-sizing:border-box}
  html,body{width:794px;height:1200px;overflow:hidden;background:var(--paper)}
  body{position:relative;font-family:"Arimo",Arial,sans-serif;color:var(--ink)}
  .abs{position:absolute}
  .header-shape{position:absolute;left:0;top:0}
  .name{left:276px;top:103px;font-size:36px;letter-spacing:3.2px;color:var(--paper);font-weight:400;white-space:nowrap}
  .job-title{left:276px;top:150px;font-size:19px;letter-spacing:2.4px;color:var(--paper);white-space:nowrap}
  .social{left:659px;width:28px;height:28px;border:3px solid var(--paper);border-radius:50%;
    background:var(--dark);color:var(--paper);font-size:7px;display:flex;align-items:center;justify-content:center}
  .contact-icon{left:305px;width:24px;height:24px;border-radius:50%;background:var(--dark);display:flex;align-items:center;justify-content:center}
  .contact-text{left:349px;font-size:11px;letter-spacing:1.3px;white-space:nowrap}
  .personal{left:571px;font-family:"Open Sans",Arial,sans-serif;font-size:11.5px;white-space:nowrap}
  .profile-link{left:552px;top:301px;width:250px;height:35px;border-radius:9px 0 0 9px;background:var(--dark);
    color:var(--paper);font-family:"Open Sans",Arial,sans-serif;font-size:11px;line-height:13.5px;padding:4px 0 0 4px}
  .profile-link .url{display:block;padding-left:19px;position:relative}
  .profile-link .url::before,.profile-link .url::after{content:"";position:absolute;top:1px;width:12px;border-top:1px solid var(--paper)}
  .profile-link .url::before{left:3px}
  .profile-link .url::after{left:220px}
  .section-bar{background:var(--dark);color:var(--paper);font-size:20px;letter-spacing:2.6px;display:flex;align-items:center}
  .section-bar .icon{position:absolute;top:50%;transform:translateY(-50%)}
  .body-text{font-size:10.6px;letter-spacing:1.45px;line-height:13.3px;white-space:nowrap}
  .skill{font-size:12.6px;letter-spacing:1.5px;line-height:15.5px;white-space:nowrap}
  .lang-name{left:60px;font-size:13.5px;letter-spacing:1.8px}
  .dots{left:164px;display:flex;gap:8.5px}
  .dot{width:10px;height:10px;border-radius:50%;background:var(--ink)}
  .dot.off{background:var(--muted)}
  .edu-school{font-size:14px;letter-spacing:1.7px;white-space:nowrap}
  .edu-degree{font-size:12.5px;letter-spacing:1.4px;white-space:nowrap}
  .edu-years{font-size:14.5px;letter-spacing:1.7px;white-space:nowrap}
  .divider{display:inline-block;width:3px;height:13px;background:var(--ink);vertical-align:middle}
  .exp-company{left:356px;font-weight:700;font-size:13.8px;letter-spacing:1.8px;white-space:nowrap}
  .exp-role{font-size:11px;letter-spacing:1.5px;white-space:nowrap}
  .exp-date{left:356px;font-size:13.5px;letter-spacing:1.6px;white-space:nowrap}
  .exp-desc{left:357px;font-size:11px;letter-spacing:1.45px;line-height:14px;white-space:nowrap}
  .footer-band{left:0;top:1076px;width:794px;height:38px;background:var(--dark)}
  .corner-rule{left:749px;top:1163px;width:1px;height:37px;background:#888}
</style>
</head>
<body>

<svg class="header-shape" width="794" height="310" viewBox="0 0 794 310" aria-hidden="true">
  <path d="M0 0H794V219H342C300 219 282 228 258 258C232 290 212 306 168 306H0Z" fill="var(--dark)"/>
  <circle cx="143" cy="152" r="101" fill="none" stroke="var(--paper)" stroke-width="5.5"/>
</svg>
<div class="abs" role="img" aria-label="Portrait photo of the candidate" style="left:59px;top:68px;width:168px;height:168px;border-radius:50%;background:var(--photo)"></div>

<div class="abs name">Wei-Lin Hsu</div>
<div class="abs job-title">SALES MANAGER</div>

<div class="abs social" style="top:56px">Hi</div>
<div class="abs social" style="top:103px">Pix</div>
<div class="abs social" style="top:150px">Chat</div>

<div class="abs contact-icon" style="top:237px">
  <svg width="14" height="10" viewBox="0 0 14 10" aria-hidden="true"><rect x=".6" y=".6" width="12.8" height="8.8" fill="none" stroke="#fff" stroke-width="1.1"/><path d="M.6 .6L7 5.6L13.4 .6" fill="none" stroke="#fff" stroke-width="1.1"/></svg>
</div>
<div class="abs contact-icon" style="top:266px">
  <svg width="12" height="15" viewBox="0 0 12 15" aria-hidden="true"><path d="M6 0C2.7 0 0 2.6 0 5.8C0 9.8 6 15 6 15S12 9.8 12 5.8C12 2.6 9.3 0 6 0Z" fill="#fff"/><circle cx="6" cy="5.6" r="2.2" fill="var(--dark)"/></svg>
</div>
<div class="abs contact-icon" style="top:295px">
  <svg width="9" height="15" viewBox="0 0 9 15" aria-hidden="true"><rect x=".6" y=".6" width="7.8" height="13.8" rx="1.2" fill="none" stroke="#fff" stroke-width="1.2"/><rect x="1.8" y="2.2" width="5.4" height="9" fill="#fff"/></svg>
</div>
<div class="abs contact-text" style="top:242px">xxxxx@mailhub.com</div>
<div class="abs contact-text" style="top:271px">xxxxxxxx, Germany</div>
<div class="abs contact-text" style="top:300px">+ x (xxx) xxxx</div>

<div class="abs personal" style="top:240px">Date &amp; Place of birth :  xxxxxxx</div>
<div class="abs personal" style="top:270px">Nationality : Taiwanese</div>
<div class="abs profile-link">For more information, please visit my ProLink<span class="url">https://www.prolink.example/in/xxxx</span></div>

<!-- Profile -->
<div class="abs section-bar" style="left:0;top:347px;width:298px;height:32px;padding-left:58px">PROFILE
  <svg class="icon" style="left:259px" width="18" height="18" viewBox="0 0 18 18" aria-hidden="true"><circle cx="9" cy="5" r="4.2" fill="#fff"/><path d="M1.5 18C1.5 12.5 4.5 10.5 9 10.5S16.5 12.5 16.5 18Z" fill="#fff"/></svg>
</div>
<p class="abs body-text" style="left:20px;top:397px">Currently, I am a “Sales manager Asia” of<br>a top German rotary table company. I am<br>in charge of four countries Japan, China,<br>South Korea and Taiwan with 3 agents,<br>more than 20 salemen team.</p>
<p class="abs body-text" style="left:20px;top:477px">As a director of manufacuturing, I have<br>more than 5 years professional experi-<br>ences in manufacturing metal components<br>by different CNC-machines. I am capable<br>of coding CNC G,M-code, designing the<br>working path of different parts and man-<br>aging the whole process.I have well-un-<br>derstanding of mechanical outsourcing<br>ecosystem in Taiwan. With deep knowl-<br>edge of outsourcing metal components<br>to different suppliers in Taiwan.</p>
<p class="abs body-text" style="left:20px;top:637px">Familiar with coordinating with different<br>industrial processes in order to build the<br>final products. (Black oxidizing, Different<br>anodizing, Chemical polishing, Manga-<br>nese phosphate coating, Heat treatment,<br>and Different grinding methods) Especial-<br>ly love to build prototype in order to get a<br>high profitable potential products. (from<br>zero to one)</p>

<!-- Skills -->
<div class="abs section-bar" style="left:1px;top:765px;width:298px;height:34px;padding-left:58px">SKILLS
  <svg class="icon" style="left:259px" width="20" height="20" viewBox="0 0 20 20" aria-hidden="true"><g fill="#fff"><circle cx="10" cy="10" r="6.5"/><rect x="8" y="0" width="4" height="20" rx="1"/><rect x="0" y="8" width="20" height="4" rx="1"/><rect x="8" y="0" width="4" height="20" rx="1" transform="rotate(45 10 10)"/><rect x="8" y="0" width="4" height="20" rx="1" transform="rotate(-45 10 10)"/></g><circle cx="10" cy="10" r="2.8" fill="var(--dark)"/></svg>
</div>
<p class="abs skill" style="left:19px;top:809px">Great experiences in handling business<br>with Chinese-cultural business firms.</p>
<p class="abs skill" style="left:20px;top:846px">Multi-national corporation skills<br>(especially in Chinese-speakingmarket)</p>
<div class="abs skill" style="left:20px;top:888px">OEM skills</div>
<div class="abs" style="left:143px;top:888px;width:3px;height:14px;background:var(--ink)"></div>
<div class="abs skill" style="left:188px;top:889px">Trade skills</div>

<!-- Language -->
<div class="abs section-bar" style="left:0;top:916px;width:299px;height:33px;padding-left:58px">LANGUAGE
  <svg class="icon" style="left:259px" width="20" height="19" viewBox="0 0 20 19" aria-hidden="true"><path d="M10 1C4.8 1 1 4.5 1 8.6C1 10.8 2 12.6 3.7 13.9L2.8 18L7 15.8C8 16.1 9 16.2 10 16.2C15.2 16.2 19 12.7 19 8.6S15.2 1 10 1Z" fill="#fff"/><g fill="var(--dark)"><circle cx="6.5" cy="8.6" r="1.1"/><circle cx="10" cy="8.6" r="1.1"/><circle cx="13.5" cy="8.6" r="1.1"/></g></svg>
</div>
<div class="abs lang-name" style="top:968px">Chinese</div>
<div class="abs dots" style="top:972px"><span class="dot"></span><span class="dot"></span><span class="dot"></span><span class="dot"></span><span class="dot"></span></div>
<div class="abs lang-name" style="top:997px">English</div>
<div class="abs dots" style="top:1001px"><span class="dot"></span><span class="dot"></span><span class="dot"></span><span class="dot"></span><span class="dot off"></span></div>
<div class="abs lang-name" style="top:1026px">German</div>
<div class="abs dots" style="top:1030px"><span class="dot"></span><span class="dot"></span><span class="dot"></span><span class="dot"></span><span class="dot off"></span></div>

<!-- Education -->
<div class="abs section-bar" style="left:349px;top:347px;width:445px;height:34px;padding-left:29px">EDUCATION
  <svg class="icon" style="left:274px" width="28" height="20" viewBox="0 0 28 20" aria-hidden="true"><path d="M14 1L1 7L14 13L27 7Z" fill="#fff"/><path d="M6 10V16C9 19 19 19 22 16V10L14 14Z" fill="#fff"/></svg>
</div>
<div class="abs edu-school" style="left:357px;top:399px">Tamsui Valley University</div>
<div class="abs" style="left:617px;top:400px;width:3px;height:14px;background:var(--ink)"></div>
<div class="abs edu-years" style="left:628px;top:398px">2005 - 2009</div>
<div class="abs edu-degree" style="left:379px;top:418px">Bachelor of Chemical engineering</div>
<div class="abs edu-school" style="left:357px;top:447px">Politecnico Arcadia Italy</div>
<div class="abs" style="left:617px;top:449px;width:3px;height:14px;background:var(--ink)"></div>
<div class="abs edu-years" style="left:628px;top:448px">2011 - 2012</div>
<div class="abs edu-degree" style="left:379px;top:467px">Master of Business Administration</div>

<!-- Experience -->
<div class="abs section-bar" style="left:348px;top:504px;width:445px;height:33px;padding-left:29px">EXPERIENCE
  <svg class="icon" style="left:276px" width="22" height="20" viewBox="0 0 22 20" aria-hidden="true"><rect x="0" y="0" width="22" height="14" rx="1" fill="#fff"/><rect x="2" y="2" width="18" height="9" fill="var(--dark)"/><rect x="9" y="14" width="4" height="4" fill="#fff"/><rect x="5" y="17" width="12" height="2.5" fill="#fff"/></svg>
</div>

<div class="abs exp-company" style="top:555px">Asiaxxxxxxxxx</div>
<div class="abs" style="left:590px;top:556px;width:3px;height:15px;background:var(--ink)"></div>
<div class="abs exp-role" style="left:608px;top:557px">Sales Manager</div>
<div class="abs exp-date" style="top:578px">2018 - Now</div>
<p class="abs exp-desc" style="left:358px;top:599px">Currently, leading 3 major dealers in Taiwan, Mainland<br>China, South Korea and Japan with more than 20 sales-<br>men team.<br>Drehwerk provides rotary tables, trunnions and 2 axis<br>rotary tilt units shall have the best possible technical<br>characteristics in the smallest possible space, is the<br>principle model for our dividing heads -engineering<br>-manufacturing -and assembly.</p>

<div class="abs exp-company" style="top:724px">Hengli Precision Machinery</div>
<div class="abs" style="left:590px;top:725px;width:3px;height:15px;background:var(--ink)"></div>
<div class="abs exp-role" style="left:607px;top:726px">Director of Manufacturing</div>
<div class="abs exp-date" style="top:742px">2012 - 2017</div>
<p class="abs exp-desc" style="top:762px">Using CNC turn/mill machine to manufacture any mechan-<br>ical components as customers want. Also providing great<br>total solutions for our clients.<br>Photos shown in my ProLink are my products which are<br>made by CNC turn-milling dual spindles machines(trophy<br>is programmed by CAM).</p>

<div class="abs exp-company" style="top:862px">Brightway Import Mannheim</div>
<div class="abs" style="left:590px;top:863px;width:3px;height:15px;background:var(--ink)"></div>
<div class="abs exp-role" style="left:607px;top:864px">Marketing Analyst</div>
<div class="abs exp-date" style="top:883px">2012 Apr - 2012 Nov</div>
<p class="abs exp-desc" style="top:903px">Help Brightway Import to build their sales/marketing<br>strategy for the new launched product “Slick-Mend” in<br>central Europe.</p>

<div class="abs exp-company" style="top:961px">Calcestra Group Bergamo</div>
<div class="abs" style="left:590px;top:962px;width:3px;height:15px;background:var(--ink)"></div>
<div class="abs exp-role" style="left:608px;top:963px">External consultant</div>
<div class="abs exp-date" style="left:357px;top:982px">2011 Oct - 2012 Mar</div>
<p class="abs exp-desc" style="top:1001px">To improve the Vanta suite(ERP system) of Calce-<br>stra with re-organized procurement process and new<br>standardized KPIs.</p>

<div class="abs footer-band"></div>
<div class="abs corner-rule"></div>

</body>
</html>
```